Crimson Ledger.com is wanting to create a Facebook Ad to attract buyers to come to their website. We are wanting buyers to register for free and create an account on Crimson Ledger. com. We want to increase the number of buyers by posting an ad on Facebook groups. The buyer will click the link to our websites registration page.
https://www.crimsonledger.com/account/users/register

Semi Trucks
Semi Trailers
Construction Equipment
Farm Equipment
Trailers
ATV/UTV
Boats
RVs

```html
<!DOCTYPE html>
<html lang="en">
<head>
<meta charset="utf-8">
<title>Crimson Ledger.com – Register Free</title>
<link rel="stylesheet" href="https://fonts.googleapis.com/css2?family=Montserrat:wght@700;800&family=Rubik:ital,wght@1,500&display=swap">
<style>
  :root {
    --orange: #e3611f;
    --orange-dark: #a8410f;
    --ink: #1b1b1b;
    --list-ink: #2a2a2a;
    --paper: #ffffff;
    --haze: #ececec;
    --frame-dark: #151515;
  }
  * { margin: 0; padding: 0; box-sizing: border-box; }
  html, body { width: 1200px; height: 1200px; overflow: hidden; background: var(--paper); }
  .ad {
    position: relative;
    width: 1200px;
    height: 1200px;
    overflow: hidden;
    background: linear-gradient(180deg, var(--paper) 0%, var(--paper) 45%, #f1f1f1 70%, var(--paper) 100%);
  }
  .ad-shapes { position: absolute; inset: 0; z-index: 0; }
  .brand {
    position: absolute;
    z-index: 1;
    left: 70px;
    top: 120px;
    display: flex;
    align-items: center;
    gap: 22px;
  }
  .brand-mark { width: 44px; height: 44px; background: var(--orange); }
  .brand-name {
    font-family: "Montserrat", sans-serif;
    font-weight: 800;
    font-size: 54px;
    line-height: 1.05;
    color: var(--ink);
    text-transform: uppercase;
  }
  .category-list {
    position: absolute;
    z-index: 1;
    left: 84px;
    top: 496px;
    list-style: none;
    font-family: "Rubik", sans-serif;
    font-style: italic;
    font-weight: 500;
    font-size: 35px;
    color: var(--list-ink);
  }
  .category-list li {
    height: 52.5px;
    display: flex;
    align-items: center;
    white-space: nowrap;
  }
  .category-list li::before {
    content: "";
    width: 0; height: 0;
    border-top: 8px solid transparent;
    border-bottom: 8px solid transparent;
    border-left: 12px solid var(--orange);
    margin-right: 18px;
  }
  .register-label {
    position: absolute;
    z-index: 1;
    left: 75px;
    top: 982px;
    font-family: "Montserrat", sans-serif;
    font-weight: 700;
    font-size: 34px;
    color: var(--paper);
  }
  .register-url {
    position: absolute;
    z-index: 1;
    left: 98px;
    top: 1087px;
    font-family: "Montserrat", sans-serif;
    font-weight: 700;
    font-size: 32px;
    color: var(--paper);
    white-space: nowrap;
  }
</style>
</head>
<body>
<main class="ad">
  <svg class="ad-shapes" width="1200" height="1200" viewBox="0 0 1200 1200">
    <defs>
      <linearGradient id="haze-fill" x1="0" y1="0" x2="1" y2="1">
        <stop offset="0" stop-color="#f4f4f4"/>
        <stop offset="1" stop-color="#dcdcdc"/>
      </linearGradient>
      <radialGradient id="frame-fill" cx="0.5" cy="0.5" r="0.6">
        <stop offset="0" stop-color="#3a3320"/>
        <stop offset="1" stop-color="#151515"/>
      </radialGradient>
      <linearGradient id="hero-fill" x1="0" y1="0" x2="0" y2="1">
        <stop offset="0" stop-color="#4b86d8"/>
        <stop offset="0.35" stop-color="#c9a21c"/>
        <stop offset="0.7" stop-color="#6b5a35"/>
        <stop offset="1" stop-color="#8c7448"/>
      </linearGradient>
      <linearGradient id="thumb-trailer" x1="0" y1="0" x2="0" y2="1">
        <stop offset="0" stop-color="#4e7a3e"/>
        <stop offset="1" stop-color="#7a6a5a"/>
      </linearGradient>
      <linearGradient id="thumb-truck" x1="0" y1="0" x2="0" y2="1">
        <stop offset="0" stop-color="#6d8fb4"/>
        <stop offset="0.5" stop-color="#e2e2e2"/>
        <stop offset="1" stop-color="#9a968e"/>
      </linearGradient>
      <linearGradient id="thumb-digger" x1="0" y1="0" x2="0" y2="1">
        <stop offset="0" stop-color="#8a7a62"/>
        <stop offset="1" stop-color="#d4a418"/>
      </linearGradient>
      <clipPath id="hero-clip"><circle cx="910" cy="337" r="302"/></clipPath>
    </defs>

    <rect class="backdrop-haze" x="0" y="560" width="720" height="520" fill="url(#haze-fill)" opacity="0.55" role="img" aria-label="Faded photo of heavy machinery parts"/>

    <circle class="hero-frame" cx="935" cy="385" r="415" fill="url(#frame-fill)" role="img" aria-label="Darkened close-up of a yellow excavator"/>

    <circle cx="910" cy="337" r="310" fill="var(--paper)"/>
    <rect x="600" y="0" width="620" height="660" fill="url(#hero-fill)" clip-path="url(#hero-clip)" role="img" aria-label="Photo of a used yellow excavator on dirt ground under a blue sky"/>

    <polygon class="register-band" points="0,970 387,970 380,1041 0,1041" fill="var(--orange)"/>
    <polygon class="register-fold" points="0,1041 380,1041 80,1073 56,1073" fill="var(--orange-dark)"/>
    <polygon class="url-band" points="68,1073 1200,1073 1200,1143 56,1143" fill="var(--orange)"/>

    <g class="thumbnails">
      <path d="M460,872 H676 Q690,872 686,886 L648,1030 Q645,1041 632,1041 H428 Q414,1041 418,1027 L454,884 Q457,872 460,872 Z" fill="url(#thumb-trailer)" stroke="var(--orange)" stroke-width="5" role="img" aria-label="Photo of a flatbed trailer with a loader crane"/>
      <path d="M696,872 H912 Q926,872 922,886 L884,1030 Q881,1041 868,1041 H664 Q650,1041 654,1027 L690,884 Q693,872 696,872 Z" fill="url(#thumb-truck)" stroke="var(--orange)" stroke-width="5" role="img" aria-label="Photo of a white semi truck in a gravel lot"/>
      <path d="M933,872 H1149 Q1163,872 1159,886 L1121,1030 Q1118,1041 1105,1041 H901 Q887,1041 891,1027 L927,884 Q930,872 933,872 Z" fill="url(#thumb-digger)" stroke="var(--orange)" stroke-width="5" role="img" aria-label="Photo of a damaged yellow mini excavator"/>
    </g>
  </svg>

  <div class="brand">
    <span class="brand-mark"></span>
    <span class="brand-name">Crimson<br>Ledger</span>
  </div>

  <ul class="category-list">
    <li>Semi Trucks</li>
    <li>Semi Trailers</li>
    <li>Construction Equipment</li>
    <li>Farm Equipment</li>
    <li>Trailers</li>
    <li>ATV/UTV</li>
    <li>Boats</li>
    <li>RVs</li>
  </ul>

  <p class="register-label">Register here</p>
  <p class="register-url">https://www.crimsonledger.com/account/users/register</p>
</main>
</body>
</html>
```